Parenting Teens Book Cover Design Project

Updating my existing cover (see attached) so that it is more modern/contemporary.
The book is for Australian parents about helping their teens through their senior years of school and covers info about helping them with motivation, stress, school, parties, career decisions, conflict etc. The author (myself) is a clinical psychologist who specialises in working with teens. I sell this book through my website - see www.brightquillpress.net -(so a small version of the cover in the products section of my site still needs to look good) and back of room sales. I've sold a few thousand of these over the last 9 years but the current cover feels dated to me.
I'm looking for something with clean lines, not cluttered, modern and bold. I'm wary of teen/parent images that look "happy American sitcom" (sorry if this offends).
I've had another self published book which had an entirely black glossy cover and while this looked great, it was a nightmare to sell because the covers got very easily scratched and with faded bits.
It will be an a5 size book.
There is possibly too much font on the back cover, if it cant be made to look good, I will try to reduce it.
Please note, I am a genuine seeker, and am keen to get this design from this website, and will only go elsewhere if I really cant find what I'm looking for here.
Parents and secondary teachers
School

```html
<!DOCTYPE html>
<html lang="en">
<head>
<meta charset="utf-8">
<title>The Months that Matter – Book Cover</title>
<link href="https://fonts.googleapis.com/css2?family=Montserrat:wght@400;700&display=swap" rel="stylesheet">
<style>
  :root {
    --sky-deep: #1b3563;
    --sky-mid: #2d5a92;
    --sky-light: #9fbedb;
    --horizon: #e6edf0;
    --field: #c9a95e;
    --road-light: #6b6b6b;
    --road-dark: #3a3a3a;
    --text-white: #ffffff;
  }
  * { margin: 0; padding: 0; box-sizing: border-box; }
  html, body {
    width: 846px;
    height: 1200px;
    overflow: hidden;
    background: #ffffff;
  }
  .cover {
    position: relative;
    width: 846px;
    height: 1200px;
    overflow: hidden;
    font-family: "Montserrat", Arial, sans-serif;
    color: var(--text-white);
    text-align: center;
  }
  .cover-photo {
    position: absolute;
    inset: 0;
    background: linear-gradient(
      to bottom,
      var(--sky-deep) 0%,
      var(--sky-deep) 24%,
      var(--sky-mid) 40%,
      var(--sky-light) 52%,
      var(--horizon) 60%,
      var(--field) 66%,
      var(--road-light) 76%,
      var(--road-dark) 100%
    );
  }
  .author {
    position: absolute;
    top: 78px;
    left: 0;
    right: 0;
    font-size: 27px;
    font-weight: 400;
    letter-spacing: 0.3px;
  }
  .title {
    position: absolute;
    top: 162px;
    left: 0;
    right: 0;
    font-size: 108px;
    font-weight: 700;
    line-height: 102px;
    letter-spacing: -2px;
    white-space: nowrap;
  }
  .subtitle {
    position: absolute;
    top: 440px;
    left: 0;
    right: 0;
    font-size: 25px;
    font-weight: 400;
    line-height: 32px;
  }
</style>
</head>
<body>
  <main class="cover">
    <div class="cover-photo" role="img" aria-label="Photograph of a parent and young child sitting together on an empty country road stretching to the horizon, with golden fields and a blue cloudy sky"></div>
    <p class="author">Maren Ashdown</p>
    <h1 class="title">The Months<br>that Matter</h1>
    <p class="subtitle">Build Drive, Results<br>and Confidence in Your Senior<br>School Student</p>
  </main>
</body>
</html>
```